Business Card for Brenwick Painting

We need a simple, yet out standing business card for our painting company.

Target Market(s)

wealthy; high-end neighborhoods, and businesses

Industry/Entity Type

Painting

Contact Information for Business Card

Name:
Dorian Vask

Email:
d.vask@brenwick-painting.example

Website:
Brenwick-painting.example

Phone Number:
(555) 412-9063

Font styles to use
Serif
Sans Serif

Requirements
Must have
• slogan "making change simple"
Should not have
• A title attached to the name on the card

```html
<!DOCTYPE html>
<html lang="en">
<head>
<meta charset="utf-8">
<title>Brenwick Painting – Business Card</title>
<link rel="stylesheet" href="https://fonts.googleapis.com/css2?family=Open+Sans:wght@400;600&family=Roboto:wght@700&display=swap">
<style>
  :root {
    --charcoal: #2a292b;
    --charcoal-edge: #1f1e20;
    --leaf: #6a9838;
    --leaf-dark: #3b6423;
    --brand-green: #8cbf3f;
    --band: #eeeff0;
    --name-grey: #e6e8e4;
    --contact: #f2f2f2;
    --backdrop: #d9d6cc;
  }
  * { box-sizing: border-box; margin: 0; padding: 0; }
  html, body { width: 1200px; height: 800px; overflow: hidden; }
  body {
    background: var(--backdrop);
    font-family: "Open Sans", sans-serif;
    display: flex;
    align-items: center;
    justify-content: center;
    gap: 40px;
  }
  .card {
    position: relative;
    width: 540px;
    height: 309px;
    background: var(--charcoal);
    overflow: hidden;
    box-shadow: 0 6px 18px rgba(0,0,0,.25);
  }

  /* Front side */
  .front__stripe {
    position: absolute;
    top: 0; bottom: 0;
    left: 160px; width: 240px;
    background: var(--leaf);
  }
  .front__band {
    position: absolute;
    top: 112px; height: 86px;
    left: 100px; right: 100px;
    background: var(--band);
    display: flex;
    align-items: center;
    justify-content: center;
    gap: 12px;
  }
  .brand-name {
    font-family: "Open Sans", sans-serif;
    font-weight: 600;
    letter-spacing: .12em;
    text-transform: uppercase;
    color: var(--leaf-dark);
    white-space: nowrap;
  }
  .brand-mark {
    width: 14px; height: 14px;
    background: var(--leaf-dark);
  }
  .front__band .brand-name { font-size: 22px; }

  /* Back side */
  .back__panel {
    position: absolute;
    top: 0; bottom: 0;
    left: 285px; right: 0;
    background: var(--leaf);
  }
  .back__brand {
    position: absolute;
    top: 42px; left: 36px;
    display: flex;
    align-items: center;
    gap: 10px;
  }
  .back__brand .brand-name { font-size: 17px; color: var(--brand-green); }
  .back__brand .brand-mark { background: var(--brand-green); width: 12px; height: 12px; }
  .person-name {
    position: absolute;
    top: 58px; left: 285px; right: 0;
    text-align: center;
    font-family: "Roboto", sans-serif;
    font-weight: 700;
    font-size: 30px;
    color: var(--name-grey);
  }
  .slogan-band {
    position: absolute;
    top: 128px; height: 46px;
    left: 240px; right: 0;
    background: var(--band);
    display: flex;
    align-items: center;
    justify-content: center;
  }
  .slogan {
    font-family: "Roboto", sans-serif;
    font-weight: 700;
    font-size: 20px;
    color: var(--leaf-dark);
  }
  .contact-list {
    position: absolute;
    left: 36px; bottom: 30px;
    list-style: none;
    color: var(--contact);
    font-size: 14px;
    line-height: 24px;
  }
  .contact-list li { display: flex; align-items: center; gap: 10px; }
  .contact-list svg { width: 12px; height: 12px; flex: none; fill: none; stroke: var(--contact); stroke-width: 1.6; }
</style>
</head>
<body>

<section class="card card--front" aria-label="Card front">
  <div class="front__stripe"></div>
  <div class="front__band">
    <span class="brand-mark"></span>
    <span class="brand-name">Brenwick Painting</span>
  </div>
</section>

<section class="card card--back" aria-label="Card back">
  <div class="back__panel"></div>
  <div class="back__brand">
    <span class="brand-mark"></span>
    <span class="brand-name">Brenwick Painting</span>
  </div>
  <h1 class="person-name">Dorian Vask</h1>
  <div class="slogan-band"><p class="slogan">Making change simple</p></div>
  <ul class="contact-list">
    <li>
      <svg viewBox="0 0 12 12"><path d="M3 1 L5 3.5 L4 5 Q5.5 7.5 7 8 L8.5 7 L11 9 L9.5 11 Q4 10.5 1 3 Z"/></svg>
      (555) 412-9063
    </li>
    <li>
      <svg viewBox="0 0 12 12"><circle cx="6" cy="6" r="5"/><ellipse cx="6" cy="6" rx="2.2" ry="5"/><path d="M1 6 H11"/></svg>
      Brenwick-painting.example
    </li>
    <li>
      <svg viewBox="0 0 12 12"><rect x="1" y="2.5" width="10" height="7"/><path d="M1 2.5 L6 6.5 L11 2.5"/></svg>
      d.vask@brenwick-painting.example
    </li>
  </ul>
</section>

</body>
</html>
```